Medical Office Needs an Updated Treatment Brochure

We need an updated brochure for a new treatment our offices are offering. The old brochure attached has all the current information on it, it just needs a new design.
We would like the updated version to be more modern and sleek as well as engaging.
Please see the old brochure attached for reference as well as this link: http://www.lumarvessa.com/medspa/iv-therapy/#1
The content from the attached brochure will remain.
UPDATE**** PLEASE SEE THE ATTACHED EXAMPLE BROCHURE OF THE DESIGN WE ARE LOOKING FOR!!
Thank you!!
Medical

```html
<!DOCTYPE html>
<html lang="en">
<head>
<meta charset="utf-8">
<title>Lumarvessa – IV Nutrient Therapy Brochure</title>
<link href="https://fonts.googleapis.com/css2?family=Playfair+Display:ital,wght@0,400;0,700;1,400&family=Andika&family=Arimo:wght@400;700&display=swap" rel="stylesheet">
<style>
:root{
  --stage:#b2b8b8;
  --magenta:#a9386a;
  --magenta-soft:#c9768f;
  --pink-soft:#e7b8c8;
  --green:#8fca8c;
  --green-pale:#e4f1d3;
  --cream:#f4f6dc;
  --ink:#3d3d3d;
  --white:#ffffff;
  --serif:"Playfair Display", Georgia, serif;
  --quote:"Andika", "Trebuchet MS", sans-serif;
  --sans:"Arimo", Arial, sans-serif;
}
*{box-sizing:border-box;margin:0;padding:0}
html,body{width:812px;height:1200px;overflow:hidden;background:var(--stage)}
.canvas{position:relative;width:812px;height:1200px}
.spread{position:absolute;overflow:hidden;box-shadow:0 3px 8px rgba(0,0,0,.3);background:var(--white)}
.spread--outside{left:62px;top:52px;width:685px;height:526px}
.spread--inside{left:55px;top:618px;width:691px;height:532px}
.panel{position:absolute;top:0;height:100%;overflow:hidden}
.shape{position:absolute;left:0;top:0;width:100%;height:100%}
.abs{position:absolute}
.heading{font-family:var(--serif);font-weight:700;color:var(--green);font-size:23px;line-height:1.2}
.heading--magenta{color:var(--magenta);font-size:16px}
.heading--green-sm{color:var(--green);font-size:18px}
.rule{position:absolute;height:3px;width:43px;background:var(--pink-soft)}
.rule--green{background:var(--green)}
.rule--magenta{background:var(--magenta-soft)}
.subhead{font-family:var(--serif);font-style:italic;font-weight:400;color:var(--magenta);font-size:15px;line-height:1.2}
.subhead--dark{color:#4c5a4a}
.body{font-family:var(--sans);font-size:7.6px;line-height:1.4;color:var(--ink)}
.body p+p{margin-top:10px}
.body b{font-weight:400;color:#1f6a2c}
.quote{font-family:var(--quote);color:var(--white);font-size:16px;text-align:center;line-height:20px;letter-spacing:.3px}
.contact{font-family:var(--sans);color:var(--white);font-size:7px;font-weight:700;line-height:1.35}
.contact h3{font-size:10.5px;font-weight:700}
.contact p+h3{margin-top:11px}
.contact .web{margin-top:12px}
.brand{font-family:var(--serif);font-weight:400;color:var(--green);font-size:34px;display:flex;align-items:center;gap:8px}
.brand-dot{width:14px;height:14px;border-radius:50%;background:var(--pink-soft)}
.brand-sub{font-family:var(--sans);font-size:5px;color:var(--magenta-soft);letter-spacing:.4px}
.title{font-family:var(--serif);font-weight:700;color:var(--magenta);font-size:37px;line-height:1.02}
.tagline{font-family:var(--serif);font-style:italic;color:var(--magenta);font-size:11px}
.offers{display:grid;grid-template-columns:1fr 1fr;row-gap:13px;column-gap:6px}
.offer{display:flex;align-items:center;gap:8px;font-family:var(--sans);font-size:10px;color:var(--magenta-soft)}
.offer-icon{width:20px;height:20px;border-radius:50%;flex:none}
</style>
</head>
<body>
<div class="canvas">

  <section class="spread spread--outside">
    <div class="panel" style="left:0;width:228px">
      <svg class="shape" viewBox="0 0 228 526" preserveAspectRatio="none">
        <defs><linearGradient id="factsBand" x1="0" y1="0" x2="0" y2="1"><stop offset="0" stop-color="#cf8aa2"/><stop offset="1" stop-color="#a9386a"/></linearGradient></defs>
        <path d="M0 400 L228 400 L228 526 L0 526Z" fill="url(#factsBand)"/>
        <path d="M228 0 L228 250 C228 330 200 395 120 400 L0 402 L0 526 L228 526Z" fill="url(#factsBand)"/>
      </svg>
      <h2 class="heading abs" style="left:26px;top:72px">The Facts</h2>
      <div class="rule" style="left:30px;top:105px"></div>
      <h3 class="subhead abs" style="left:30px;top:134px">What is IV Therapy?</h3>
      <div class="body abs" style="left:30px;top:180px;width:174px;font-size:8.2px;line-height:10.6px">
        <p>IV Nutrient Therapy involves the direct administration of vital minerals, nutrients and vitamins directly into the bloodstream (intravenously infused) through an IV drip.</p>
        <p>These essential nutrients can help boost immune function, increase energy levels, assist in weight management, avoid chronic health issues, and even aid in skin rejuvenation.</p>
      </div>
      <p class="quote abs" style="left:14px;top:432px;width:202px">“IV Therapy is great for boosting health and preventing illness.”</p>
    </div>

    <div class="panel" style="left:228px;width:229px">
      <svg class="shape" viewBox="0 0 229 526" preserveAspectRatio="none">
        <defs><linearGradient id="contactBg" x1="0" y1="0" x2="0" y2="1"><stop offset="0" stop-color="#a9386a"/><stop offset="1" stop-color="#d596a8"/></linearGradient></defs>
        <rect width="229" height="526" fill="url(#contactBg)"/>
        <path d="M0 526 L0 470 C20 420 60 410 110 420 C160 430 200 400 229 380 L229 526Z" fill="#e8f2d6"/>
      </svg>
      <div class="contact abs" style="left:20px;top:282px;width:205px">
        <h3>Lumarvessa</h3>
        <p>2710 Orchard Way<br>Cedarline CA 91742</p>
        <h3>Lumarvessa Southwest</h3>
        <p>8135 Linden Avenue, Suite 214<br>Cedarline, CA 91748</p>
        <p class="web">W: www.lumarvessa.com<br>E: appointments@lumarvessa.com<br>P: 844-Lumarvessa</p>
      </div>
    </div>

    <div class="panel" style="left:457px;width:228px">
      <svg class="shape" viewBox="0 0 228 526" preserveAspectRatio="none">
        <defs>
          <linearGradient id="coverBg" x1="0" y1="0" x2="0" y2="1"><stop offset="0" stop-color="#f7f7e0"/><stop offset="1" stop-color="#d9ecbf"/></linearGradient>
          <linearGradient id="coverPhoto" x1="0" y1="0" x2="1" y2="1"><stop offset="0" stop-color="#3d5f78"/><stop offset=".6" stop-color="#8aa0c8"/><stop offset="1" stop-color="#b7a6d8"/></linearGradient>
        </defs>
        <rect width="228" height="526" fill="url(#coverBg)"/>
        <path d="M0 385 C30 320 110 330 160 310 C200 294 218 280 228 270 L228 526 L0 526Z" fill="#e3b9c9"/>
        <path d="M0 398 C32 334 112 346 162 324 C200 308 218 296 228 288 L228 526 L0 526Z" fill="url(#coverPhoto)" role="img" aria-label="Photo of an IV drip chamber with soft blurred lights behind it"/>
      </svg>
      <div class="abs" style="left:14px;top:72px">
        <div class="brand">Lumarvessa<span class="brand-dot"></span></div>
        <div class="brand-sub">COSMETIC SURGERY AND MEDICAL AESTHETICS</div>
      </div>
      <h1 class="title abs" style="left:17px;top:155px">IV Nutrient<br>Therapy</h1>
      <p class="tagline abs" style="left:21px;top:243px">Revitalize, Recharge and Rejuvenate!</p>
    </div>
  </section>

  <section class="spread spread--inside">
    <div class="panel" style="left:0;width:230px">
      <svg class="shape" viewBox="0 0 230 532" preserveAspectRatio="none">
        <defs><linearGradient id="ingBg" x1="0" y1="0" x2="0" y2="1"><stop offset="0" stop-color="#f2e7d8"/><stop offset="1" stop-color="#dba6bd"/></linearGradient></defs>
        <rect width="230" height="532" fill="#fff"/>
        <path d="M0 210 C40 180 120 180 180 160 C210 150 225 130 230 110 L230 532 L0 532Z" fill="#dcefd2"/>
        <path d="M0 222 C45 192 125 195 185 172 C212 162 226 145 230 128 L230 532 L0 532Z" fill="url(#ingBg)"/>
      </svg>
      <h2 class="heading abs" style="left:22px;top:24px;color:var(--magenta-soft);font-size:19px">Ingredients</h2>
      <div class="rule rule--green" style="left:22px;top:54px"></div>
      <h3 class="subhead abs" style="left:22px;top:73px">What’s in it?</h3>
      <div class="body abs" style="left:29px;top:96px;width:174px;font-size:9px;line-height:12px">
        <p>A number of nutrients play well-defined roles in the maintenance of a robust immune response, optimal energy, and overall health.</p>
      </div>
      <h3 class="subhead abs" style="left:29px;top:189px;width:180px;font-size:14px;line-height:18px">Some of the amazing<br>vitamins we use:</h3>
      <div class="body abs" style="left:29px;top:229px;width:168px;font-size:8.2px;line-height:10.8px">
        <p><b>Magnesium</b>: Many people are lacking in this essential mineral. Magnesium is an excellent therapy for patients with heart disease, respiratory problems, migraines, and more. It helps with arrhythmias and can arrest an acute asthma attack. IV magnesium is also very relaxing, something we could all use.</p>
        <p><b>Vitamin C</b>: IV administration fights off foreign invaders in your body and acts as a potent anti-histamine. From infections to cancer, the evidence of its powerful influence is simply astonishing when administered IV and in doses far too high for oral intake.</p>
        <p><b>Glutathione</b>: This is the major super-antioxidant and detoxifying agent of our body. It cannot be taken orally but is made in the body. Whey protein and other nutritionals can help build glutathione in the body. It is severely depleted by mercury and chemicals. Many people exist with glutathione deficiency.</p>
      </div>
    </div>

    <div class="panel" style="left:230px;width:230px">
      <svg class="shape" viewBox="0 0 230 532" preserveAspectRatio="none">
        <defs>
          <linearGradient id="suiteBottom" x1="0" y1="0" x2="0" y2="1"><stop offset="0" stop-color="#f7f7e4"/><stop offset="1" stop-color="#cfe6b6"/></linearGradient>
          <linearGradient id="suitePhoto" x1="0" y1="0" x2="1" y2="1"><stop offset="0" stop-color="#9fc0d8"/><stop offset=".55" stop-color="#c9b59a"/><stop offset="1" stop-color="#7fa35a"/></linearGradient>
        </defs>
        <rect width="230" height="532" fill="#fff"/>
        <rect y="302" width="230" height="230" fill="url(#suiteBottom)"/>
        <rect y="299" width="230" height="5" fill="var(--magenta-soft)"/>
        <path d="M0 0 L230 0 L230 160 C150 162 70 130 30 80 C10 55 0 25 0 0Z" fill="#b9567c"/>
        <path d="M12 0 L230 0 L230 155 C155 156 80 126 42 78 C22 52 12 25 12 0Z" fill="url(#suitePhoto)" role="img" aria-label="Photo of a smiling couple after exercise beside an IV drip with fresh fruit"/>
      </svg>
      <h2 class="heading heading--magenta abs" style="left:20px;top:166px">Our Therapeutic Suite</h2>
      <div class="rule rule--magenta" style="left:20px;top:193px;width:40px"></div>
      <div class="body abs" style="left:27px;top:206px;width:180px;font-size:7.4px;line-height:9.4px">
        <p>When you receive treatment with IV nutrients, you sit comfortably in a recliner while a sterile IV line is started and your specific composition of nutrients is infused. During this time, which usually lasts less than 50 minutes, you may opt for Plug in you PDA or LapTop and go to work, read, watch TV, nap, or simply relax. A complete treatment course often requires a series of IV infusions.</p>
      </div>
      <h2 class="heading heading--magenta abs" style="left:20px;top:321px">What We Offer</h2>
      <div class="rule rule--magenta" style="left:20px;top:347px;width:40px"></div>
      <div class="offers abs" style="left:18px;top:370px;width:200px">
        <div class="offer"><span class="offer-icon" style="background:#e6e6ea"></span>Glamour</div>
        <div class="offer"><span class="offer-icon" style="background:#2c3e7a"></span>Energy</div>
        <div class="offer"><span class="offer-icon" style="background:#efe3b0"></span>Immunity</div>
        <div class="offer"><span class="offer-icon" style="background:#7fb3e0"></span>Hydration</div>
        <div class="offer"><span class="offer-icon" style="background:#3a3a3a"></span>Weight loss</div>
        <div class="offer"><span class="offer-icon" style="background:#d0622f"></span>Detox</div>
        <div class="offer"><span class="offer-icon" style="background:#e9d9b8"></span>Hangover</div>
        <div class="offer"><span class="offer-icon" style="background:#8a7c6a"></span>Glutathione</div>
      </div>
    </div>

    <div class="panel" style="left:460px;width:231px">
      <svg class="shape" viewBox="0 0 231 532" preserveAspectRatio="none">
        <defs>
          <linearGradient id="benBg" x1="0" y1="0" x2="0" y2="1"><stop offset="0" stop-color="#f7f7e2"/><stop offset="1" stop-color="#d2e8bb"/></linearGradient>
          <linearGradient id="benQuote" x1="0" y1="0" x2="0" y2="1"><stop offset="0" stop-color="#a9386a"/><stop offset="1" stop-color="#c97592"/></linearGradient>
        </defs>
        <rect width="231" height="532" fill="url(#benBg)"/>
        <rect y="29" width="231" height="100" fill="url(#benQuote)"/>
      </svg>
      <p class="quote abs" style="left:25px;top:43px;width:180px;font-size:14.5px;line-height:17.6px">“... Super doses can be administered via IV without gastrointestinal side effects... ”</p>
      <h2 class="heading heading--green-sm abs" style="left:21px;top:143px;color:var(--magenta-soft)">Why it’s beneficial</h2>
      <div class="rule rule--green" style="left:21px;top:172px"></div>
      <h3 class="subhead subhead--dark abs" style="left:24px;top:195px;font-size:14px">Directly to the source</h3>
      <div class="body abs" style="left:24px;top:220px;width:186px;font-size:7.3px;line-height:9.5px;color:#555">
        <p>When vitamins, minerals, and other nutrients are infused intravenously (IV) they go directly into your bloodstream to fuel your cells. That means they avoid the potential loss of potency and poor absorption in the gastrointestinal (GI) tract that is a characteristic of nutrients taken orally. This makes IV nutrient administration a powerful therapy for numerous health concerns. In addition, Super doses can be administered via IV without gastrointestinal side effects, which can limit dosing. A perfect example of this is vitamin C, which can only be taken in fairly small amounts orally before causing stomach upset. In contrast, Super doses of vitamin C, which can be very beneficial for the immune system, can be administered safely and without stomach side effects with an intravenous delivery route.</p>
      </div>
      <h3 class="subhead subhead--dark abs" style="left:24px;top:393px;width:190px;font-size:14px;line-height:18px">Use IV Therapy to<br>optimize your health</h3>
      <div class="body abs" style="left:24px;top:435px;width:186px;font-size:7.3px;line-height:9.5px;color:#555">
        <p>Proactive: Even if you’re healthy, IV administration of a wide range of vitamins and minerals is an extremely effective way to boost your nutritional status, accelerate your athletic performance and prevent illness. It is especially important when flu season is around, or before and during stressful situations.</p>
      </div>
    </div>
  </section>

</div>
</body>
</html>
```